Fachgeschäft für Uhren & Schmuck benötigt Logo & Visitenkarte
Zielgruppe
Wir sind ein Fachgeschäft für Uhren & Schmuck
Aufgabenstellung
Es sollte ein gut lesbares Logo sein, verspielt modern.

```html
<!DOCTYPE html>
<html lang="de">
<head>
<meta charset="utf-8">
<title>Marbeck – Visitenkarte</title>
<link href="https://fonts.googleapis.com/css2?family=Crimson+Pro:wght@400;600&display=swap" rel="stylesheet">
<style>
  :root {
    --backdrop: #e9e9ee;
    --card: #ffffff;
    --ink: #1c1c1f;
    --ink-soft: #3a3a40;
    --shadow: rgba(30, 30, 40, 0.12);
  }
  * { margin: 0; padding: 0; box-sizing: border-box; }
  html, body {
    width: 1200px;
    height: 1200px;
    overflow: hidden;
    background: var(--backdrop);
  }
  body {
    display: flex;
    align-items: center;
    justify-content: center;
    font-family: "Crimson Pro", Georgia, serif;
    color: var(--ink);
  }
  .business-card {
    position: relative;
    width: 1000px;
    height: 580px;
    background: var(--card);
    box-shadow: 0 20px 50px var(--shadow);
    padding: 90px 80px;
  }
  .contact {
    position: absolute;
    left: 80px;
    top: 300px;
  }
  .contact__name {
    font-size: 40px;
    font-weight: 600;
    margin-bottom: 22px;
  }
  .contact__line {
    font-size: 30px;
    font-style: italic;
    line-height: 1.3;
    color: var(--ink-soft);
  }
  .brand {
    position: absolute;
    right: 80px;
    top: 110px;
    display: flex;
    align-items: center;
    gap: 22px;
  }
  .brand__dot {
    width: 16px;
    height: 16px;
    border-radius: 50%;
    background: var(--ink);
  }
  .brand__name {
    font-size: 58px;
    font-weight: 400;
    letter-spacing: 0.32em;
    color: var(--ink);
  }
</style>
</head>
<body>
  <article class="business-card">
    <div class="brand">
      <span class="brand__dot"></span>
      <span class="brand__name">MARBECK</span>
    </div>
    <div class="contact">
      <p class="contact__name">Konrad Albers</p>
      <p class="contact__line">Lindenhofweg 8</p>
      <p class="contact__line">20457 Hamburg</p>
      <p class="contact__line">albers@marbeck-uhren.de</p>
      <p class="contact__line">040-5512789012</p>
    </div>
  </article>
</body>
</html>
```